Real Estate Business Card Redesign Overall - Modern and Clean

Dear All,
I am a real estate Broker in the Texas,USA that has 2 real estate companies that I own. I wanted a clean ,cool modern look on the front with my name and contact info.

The cards can be white or dark color. I plan on using Brill Print to prin the card in the Velora Paper. If you think i should rounded corners , i can do that too.

On the back side I wanted to show both my 2 companies somehow.

KALBRIX is a Commercial Real Estate company

QLN uHomes is a Residential Real Estate Company

Target Market(s)

corporate and luxury markets

Industry/Entity Type

Real Estate

Contact Information for Business Card

Marcus P. Holt
Broker or Principal

Marcus P. Holt | RVPA, TLA®, BXO, HNK

address:
3418 Willow Fen Dr Suite 410
Brenmoor, NM 75931 (you can add USA if you want)

Font styles to use
Other font styles liked:
• arial , avantgarde

Colors
0456a4
6092c4
33b8a4
87cfc6
ffffff
474747
5c5c5c
f78f20
ec1f27

Requirements
Must have
• Marcus P. Holt
• address somewhere
• 3418 Willow Fen Dr Suite 410
• Brenmoor, NM 75931
• office phones 555.203.4417
• fax : 555.203.4418
• mobile 555.781.2290
• i have 2 emails:
• marcus@kalbrixland.example
• marcus@qlnuhomes.example
• websites:
• www.kalbrixland.example
• www.qlnuhomes.example
Nice to have
• Front of the card can be clean with just my name and contact info
• Modern and clean
• On the back we can split the 2 businesses Commercial and Residential

```html
<!DOCTYPE html>
<html lang="en">
<head>
<meta charset="utf-8">
<title>Marcus P. Holt – Business Card</title>
<link href="https://fonts.googleapis.com/css2?family=Arimo:wght@400;700&display=swap" rel="stylesheet">
<style>
  :root {
    --backdrop: #e8e8e8;
    --card-front: #353335;
    --card-back: #1e1e1e;
    --accent: #13a8ec;
  }
  * { margin: 0; padding: 0; box-sizing: border-box; }
  html, body { width: 1200px; height: 1200px; overflow: hidden; }
  body {
    background: var(--backdrop);
    font-family: "Arimo", Arial, sans-serif;
    color: var(--accent);
    position: relative;
  }
  .card {
    position: absolute;
    left: 250px;
    width: 700px;
    height: 400px;
    border-radius: 64px;
    overflow: hidden;
  }
  .card-front { top: 130px; background: var(--card-front); }
  .card-back  { top: 670px; background: var(--card-back); }

  .front-name {
    position: absolute;
    left: 90px; top: 140px;
    font-size: 50px; font-weight: 700;
    letter-spacing: 1px;
    white-space: nowrap;
  }
  .front-phone {
    position: absolute;
    left: 96px; top: 206px;
    font-size: 18px;
    letter-spacing: 14px;
  }
  .front-stripe {
    position: absolute;
    left: 600px; top: 0;
    width: 14px; height: 100%;
    background: var(--accent);
  }

  .company { position: absolute; left: 70px; }
  .company-residential { top: 62px; }
  .company-commercial { top: 128px; }
  .company-name {
    font-size: 30px; font-weight: 700;
    display: flex; align-items: center; gap: 8px;
    white-space: nowrap;
  }
  .company-mark { width: 22px; height: 22px; background: var(--accent); }
  .company-tagline { font-size: 8px; letter-spacing: 0.5px; margin-top: 2px; }

  .info-group {
    position: absolute;
    border-left: 2px solid var(--accent);
    padding-left: 12px;
    font-size: 16px;
    line-height: 1.3;
    letter-spacing: 0.8px;
    white-space: nowrap;
  }
  .info-emails { left: 300px; top: 78px; }
  .info-webs   { left: 270px; top: 168px; }
  .info-phones { left: 240px; top: 254px; }

  .office-phones {
    position: absolute;
    right: 40px; top: 56px;
    font-size: 10px;
  }
  .address {
    position: absolute;
    left: 160px; top: 340px;
    font-size: 11px;
    font-style: normal;
    letter-spacing: 3px;
    text-align: center;
    line-height: 1.4;
  }
</style>
</head>
<body>
  <section class="card card-front" aria-label="Card front">
    <h1 class="front-name">MARCUS P. HOLT</h1>
    <p class="front-phone">555.781.2290</p>
    <div class="front-stripe"></div>
  </section>

  <section class="card card-back" aria-label="Card back">
    <div class="company company-residential">
      <div class="company-name">QLN uHomes</div>
      <div class="company-tagline">RESIDENTIAL REAL ESTATE COMPANY</div>
    </div>
    <div class="company company-commercial">
      <div class="company-name"><span class="company-mark"></span>KALBRIX</div>
      <div class="company-tagline">COMMERCIAL REAL ESTATE INVESTMENTS</div>
    </div>

    <p class="office-phones">office phones 555.203.4417</p>

    <div class="info-group info-emails">
      <div>marcus@kalbrixland.example</div>
      <div>marcus@qlnuhomes.example</div>
    </div>
    <div class="info-group info-webs">
      <div>www.kalbrixland.example</div>
      <div>www.qlnuhomes.example</div>
    </div>
    <div class="info-group info-phones">
      <div>Fax : 555.203.4418</div>
      <div>Mobile 555.781.2290</div>
    </div>

    <address class="address">
      3418 Willow Fen Dr Suite 410<br>
      Brenmoor, NM 75931
    </address>
  </section>
</body>
</html>
```